RT Advisory - Web Design Upgrade

We have recently designed a website (http://www.rtadvisory-example.com.au) which requires more creative and professional inputs. The website was designed using 'bright hosting site builder template' and it is currently available for viewing on the internet. Also, you are able to access the PDF files for the 6 main pages (i.e. Home, About, Services, Contaminated Land Management, Groundwater Management and Contact).

The current website has 17 pages, however, your design may only be required for the 6 main pages.

Currently the website background is white but we are open to other colours provided the company logo is adjusted accordingly.

The idea is to upgrade the existing design and, if possible, continue using 'bright hosting' as the preferred web host. So we are not sure if the design should be coded or uncoded...we leave it to your proficiency and advice.

Target Market(s)

Government organisations, landowners and developers, waste and utilities companies, community organisations and individuals.

Font styles to use
Sans Serif

Colors
0355a3
3176b5
9ccb3b
acd037
ffffff

Requirements
Nice to have
• Sliding images

```html
<!DOCTYPE html>
<html lang="en">
<head>
<meta charset="utf-8">
<title>RT Advisory – Home</title>
<link rel="stylesheet" href="https://fonts.googleapis.com/css2?family=Lato:wght@400;700&family=Open+Sans:wght@400;600;700&display=swap">
<style>
  :root{
    --blue:#0355a3;
    --blue-mid:#3176b5;
    --blue-deep:#0a3f86;
    --green:#9ccb3b;
    --green-alt:#acd037;
    --green-dark:#4f6b1c;
    --white:#ffffff;
    --ink:#4a4a4a;
    --ink-soft:#6a6a6a;
    --rule:#d9d9d9;
  }
  *{box-sizing:border-box;margin:0;padding:0}
  html,body{width:968px;height:1200px;overflow:hidden}
  body{position:relative;font-family:"Open Sans",Arial,sans-serif;color:var(--ink);
    background:linear-gradient(#e4edfb 0,#ffffff 150px,#ffffff 100%)}
  .abs{position:absolute}

  /* header */
  .brand{left:107px;top:30px;display:flex;align-items:center;gap:12px;
    font-family:"Lato",Arial,sans-serif;font-weight:700;font-size:30px;color:var(--blue)}
  .brand-dot{width:34px;height:34px;border-radius:50%;background:var(--green)}
  .contact-strip{right:104px;top:52px;display:flex;gap:16px;font-size:11px;color:#222;align-items:center}
  .contact-strip span{display:flex;align-items:center;gap:6px}
  .contact-strip .phone{font-size:13px;font-weight:600}
  .main-nav{left:363px;top:88px;width:501px;height:41px;background:var(--blue);
    border:1px solid var(--blue-deep);box-shadow:0 14px 10px -8px rgba(0,0,0,.35);display:flex}
  .main-nav a{flex:1;display:flex;align-items:center;justify-content:center;color:var(--white);
    text-decoration:none;font-size:11px;font-weight:700;letter-spacing:.2px}
  .main-nav a+a{border-left:1px dotted rgba(255,255,255,.55)}

  /* hero */
  .hero{left:0;top:157px;width:968px;height:394px;
    background:linear-gradient(180deg,#8a8c86 0%,#b7a98a 45%,#c9b48f 75%,#a89476 100%)}
  .hero-title{left:429px;top:387px;width:435px;height:86px;background:rgba(20,20,20,.45);
    color:var(--white);font-family:"Lato",Arial,sans-serif;font-weight:700;font-size:40px;
    line-height:40px;text-align:right;padding:4px 10px 0 0;text-shadow:0 2px 3px rgba(0,0,0,.5)}
  .slider-dots{left:120px;top:463px;display:flex;gap:4px}
  .slider-dots i{width:9px;height:9px;border-radius:50%;background:var(--white);display:block}
  .slider-dots i.off{background:#bbbbbb}

  /* service cards */
  .card{top:487px;height:260px;background:var(--green);padding:6px}
  .card-1{left:105px;width:378px}
  .card-2{left:489px;width:375px}
  .card-photo{height:162px;width:100%}
  .card-1 .card-photo{background:linear-gradient(180deg,#3c4450 0%,#8a8f95 45%,#5e7a3a 70%,#2e4a22 100%)}
  .card-2 .card-photo{background:linear-gradient(180deg,#8e98a0 0%,#707070 45%,#7a4b3f 75%,#9a9a92 100%)}
  .card h2{font-family:"Lato",Arial,sans-serif;font-weight:700;font-size:17px;color:var(--white);
    margin:8px 0 0 6px;padding-bottom:3px;border-bottom:1px solid rgba(255,255,255,.7);width:255px}
  .card p{font-size:10px;line-height:13px;color:var(--white);margin:6px 6px 0}
  .read-btn{position:absolute;right:0;bottom:0;width:78px;height:22px;background:var(--blue);
    color:var(--white);font-size:11px;font-weight:700;display:flex;align-items:center;justify-content:center}

  /* welcome */
  .welcome{left:105px;top:781px;width:495px}
  .section-title{font-family:"Lato",Arial,sans-serif;font-size:20px;color:#555;font-weight:700;
    padding-bottom:9px;position:relative}
  .section-title::after{content:"";position:absolute;left:0;bottom:0;width:320px;height:1px;
    background:linear-gradient(90deg,#aaaaaa,rgba(170,170,170,0))}
  .welcome p{font-size:11.5px;line-height:17px;color:var(--ink-soft);margin-top:8px;letter-spacing:.2px}
  .welcome p:first-of-type{margin-top:14px}
  .more-link{display:block;text-align:right;font-size:11px;font-weight:600;color:var(--blue);margin-top:4px;text-decoration:none}
  .divider{left:620px;top:788px;width:1px;height:225px;background:var(--rule)}

  /* enquiry */
  .enquiry{left:640px;top:781px;width:224px}
  .enquiry .section-title::after{width:160px}
  .field{display:block;width:224px;height:28px;border:1px solid var(--rule);margin-top:4px;
    font-size:10px;color:#999;padding:7px 6px;font-family:inherit;background:var(--white)}
  .enquiry form{margin-top:20px}
  .field.msg{height:50px}
  .submit{display:block;margin-top:6px;width:80px;height:25px;background:var(--blue);color:var(--white);
    border:none;font-size:11px;font-weight:700;font-family:inherit}

  /* footer */
  .site-footer{left:0;top:1047px;width:968px;height:153px;background:var(--blue);
    border-top:3px solid #a9c6ec;color:var(--white)}
  .foot-col{position:absolute;top:20px}
  .foot-col h3{font-family:"Lato",Arial,sans-serif;font-size:16px;font-weight:700;padding-bottom:6px;
    border-bottom:1px solid rgba(255,255,255,.45);white-space:nowrap}
  .quick{left:109px;width:185px}
  .quick ul{list-style:none;display:grid;grid-template-columns:1fr 1fr;row-gap:10px;margin-top:10px;font-size:11px;font-weight:600}
  .news{left:340px;width:166px}
  .news label{display:block;font-size:11px;margin-top:10px}
  .news-row{display:flex;margin-top:4px}
  .news-row span{flex:1;height:21px;background:var(--white);color:#999;font-size:9.5px;font-style:italic;padding:4px 6px;border-radius:3px 0 0 3px}
  .news-row b{width:32px;height:21px;background:var(--green-dark);font-size:11px;display:flex;align-items:center;justify-content:center;border-radius:0 3px 3px 0}
  .contact-col{left:553px;width:138px}
  .contact-col p{display:flex;align-items:center;gap:8px;font-size:11px;margin-top:9px;white-space:nowrap}
  .contact-col p:first-of-type{margin-top:10px}
  .foot-brand{position:absolute;left:760px;top:76px;
    font-family:"Lato",Arial,sans-serif;font-weight:700;font-size:17px;color:var(--white)}
  .legal{position:absolute;left:106px;top:116px;font-size:11px;color:rgba(255,255,255,.85)}
</style>
</head>
<body>

<header>
  <div class="abs brand"><span class="brand-dot"></span>RT Advisory</div>
  <div class="abs contact-strip">
    <span><svg width="14" height="10" viewBox="0 0 14 10"><rect x=".5" y=".5" width="13" height="9" fill="none" stroke="#333"/><path d="M.5 .5 7 6 13.5 .5" fill="none" stroke="#333"/></svg>office@rtadvisory-example.com</span>
    <span class="phone"><svg width="14" height="14" viewBox="0 0 14 14"><circle cx="7" cy="7" r="6.3" fill="none" stroke="#333"/><path d="M4.5 4c0 3 2.5 5.5 5 5.5l.6-1.3-1.5-.8-.7.7c-.9-.4-1.6-1.1-2-2l.7-.7-.8-1.5z" fill="#333"/></svg>+61 (0)400 218 637</span>
  </div>
  <nav class="abs main-nav">
    <a href="#">HOME</a><a href="#">ABOUT US</a><a href="#">SERVICES</a><a href="#">CONTACT US</a>
  </nav>
</header>

<section>
  <div class="abs hero" role="img" aria-label="Slide photo: drilling crew in hi-vis working beside a yellow drill rig with steel casing pipes on stands"></div>
  <h1 class="abs hero-title">Working to Sustain our Environments</h1>
  <div class="abs slider-dots"><i></i><i></i><i class="off"></i><i></i></div>
</section>

<section>
  <article class="abs card card-1">
    <div class="card-photo" role="img" aria-label="Photo: wetland with reeds under a cloudy sunset sky"></div>
    <h2>Contaminated Land Management</h2>
    <p>Lorem ipsum dolor sit amet, consectetuer adipiscing elit, sed diam nonummy nibh euismod tinciduntm ut laoreet dolore magna aliquam..</p>
    <span class="read-btn">› Read More</span>
  </article>
  <article class="abs card card-2">
    <div class="card-photo" role="img" aria-label="Photo: two technicians in hard hats sampling a groundwater well by a roadside"></div>
    <h2>Groundwater Management</h2>
    <p>Lorem ipsum dolor sit amet, consectetuer adipiscing elit, sed diam nonummy nibh euismod tinciduntm ut laoreet dolore magna aliquam..</p>
    <span class="read-btn">› Read More</span>
  </article>
</section>

<main>
  <section class="abs welcome">
    <h2 class="section-title">Welcome to RT Advisory</h2>
    <p>Resource &amp; Terrain Advisory Pty Ltd (RT Advisory) is one of the forthcoming leading environmental consultancies operating in Australia.</p>
    <p>Our clients include national, regional and local government, landowners and developers, waste and utilities companies, community organisations and individuals.</p>
    <p>The vast majority of our work comprises repeat business from existing clients and new commissions from personal recommendations.</p>
    <p>RT Advisory's approach combines structured thinking and an awareness of the wider picture. It is based on working in partnership with clients in order to gain a clear understanding of their needs options and on-going client liaison.</p>
    <a class="more-link" href="#">Read More &gt;&gt;</a>
  </section>
  <div class="abs divider"></div>
  <section class="abs enquiry">
    <h2 class="section-title">Get in Touch</h2>
    <form>
      <span class="field">Name</span>
      <span class="field">Email</span>
      <span class="field">Phone</span>
      <span class="field msg">Message</span>
      <button class="submit" type="button">SUBMIT</button>
    </form>
  </section>
</main>

<footer class="abs site-footer">
  <div class="foot-col quick">
    <h3>QUICK LINKS</h3>
    <ul><li>&gt; Home</li><li>&gt; Services</li><li>&gt; About Us</li><li>&gt; Contact Us</li></ul>
  </div>
  <div class="foot-col news">
    <h3>NEWSLETTER</h3>
    <label>Enter your email</label>
    <div class="news-row"><span>Email Address</span><b>GO</b></div>
  </div>
  <div class="foot-col contact-col">
    <h3>CONTACT DETAILS</h3>
    <p><svg width="14" height="10" viewBox="0 0 14 10"><rect x=".5" y=".5" width="13" height="9" fill="none" stroke="#fff"/><path d="M.5 .5 7 6 13.5 .5" fill="none" stroke="#fff"/></svg>+61 (0)400 218 637</p>
    <p><svg width="14" height="14" viewBox="0 0 14 14"><circle cx="7" cy="7" r="2.6" fill="none" stroke="#fff" stroke-width="1.4"/><path d="M9.6 4.5v3.6c0 1.4 2.6 1.4 2.6-1.1A5.2 5.2 0 1 0 9.5 11.5" fill="none" stroke="#fff" stroke-width="1.4"/></svg>info@rtadvisory-example.com</p>
  </div>
  <div class="foot-brand">RT Advisory</div>
  <p class="legal">© 2014 RT Advisory &nbsp;|&nbsp; All Rights Reserved &nbsp;|&nbsp; Terms and conditions</p>
</footer>

</body>
</html>
```